I want to revise my business card design and get a more modern and up to date design.

Brolvane Handyman Sevices originated from a family-owned and operated contractor business, performing home renovation, addition, and construction work in the NYC area since 2004. Today, we specialize in reliable and affordable handyman services for residential and commercial clients In 2014, we expanded to northern New Jersey. In 2016, we brought quality home improvement and repair services to new Bucks County, PA, and nearby New Jersey areas.
Target Market(s)
Home owners and business that might be looking for a General contractor, handyman, cleaning services and Home maintenance and property.
Industry/Entity Type
Construction Company
Contact Information for Business Card
I am open to new ideas
Colors
Designer to choose colors to be used in the design.
Look and feel
Each slider illustrates characteristics of the customer's brand and the style your logo design should communicate.

```html
<!DOCTYPE html>
<html lang="en">
<head>
<meta charset="UTF-8">
<title>Brolvane Handyman Sevices – Business Card</title>
<link href="https://fonts.googleapis.com/css2?family=Questrial&display=swap" rel="stylesheet">
<style>
  :root {
    --page-bg: #e6e4e1;
    --card-top: #f7f7f6;
    --card-bottom: #e9e8e6;
    --brand-red: #d42328;
    --brand-red-dark: #a8161b;
    --ink: #1e1e1e;
    --ink-soft: #333333;
  }
  * { margin: 0; padding: 0; box-sizing: border-box; }
  html, body {
    width: 1200px; height: 970px; overflow: hidden;
    background: var(--page-bg);
    font-family: "Questrial", "Century Gothic", sans-serif;
  }
  .card {
    position: absolute; left: 60px; top: 178px;
    width: 1080px; height: 615px;
    background: linear-gradient(160deg, var(--card-top), var(--card-bottom));
    box-shadow: 0 10px 30px rgba(0,0,0,0.15);
    overflow: hidden;
  }
  .side-band {
    position: absolute; left: 0; top: 0; bottom: 0; width: 140px;
    background: linear-gradient(180deg, var(--brand-red) 0%, #e03a3a 45%, var(--brand-red-dark) 100%);
  }
  .side-rule {
    position: absolute; left: 140px; top: 0; bottom: 0; width: 5px;
    background: var(--ink);
  }
  .brand {
    position: absolute; left: 80px; top: 120px;
    display: flex; align-items: center; gap: 22px;
  }
  .brand-mark {
    width: 120px; height: 120px; border-radius: 50%;
    background: var(--brand-red);
    border: 8px solid var(--ink);
  }
  .brand-name {
    font-size: 100px; line-height: 1; color: var(--ink);
    letter-spacing: -1px;
  }
  .person-name {
    position: absolute; left: 210px; top: 392px;
    font-size: 36px; color: var(--ink); letter-spacing: 0.5px;
  }
  .name-rule {
    position: absolute; left: 210px; top: 444px; width: 795px; height: 3px;
    background: var(--brand-red);
  }
  .contacts {
    position: absolute; left: 210px; top: 466px;
    list-style: none; font-size: 26px; color: var(--ink-soft);
  }
  .contacts li { display: flex; align-items: center; gap: 10px; height: 36px; }
  .contact-icon { width: 30px; height: 30px; flex: none; }
  .services {
    position: absolute; left: 708px; top: 468px;
    display: grid; grid-template-columns: 155px 140px; row-gap: 6px;
    list-style: none; font-size: 26px; color: var(--ink);
  }
  .services li { display: flex; align-items: center; gap: 10px; }
  .services li::before {
    content: ""; width: 10px; height: 10px;
    background: var(--brand-red); transform: rotate(45deg);
  }
  .tagline {
    position: absolute; left: 210px; top: 552px;
    font-size: 26px; letter-spacing: 2px; color: var(--ink-soft);
  }
</style>
</head>
<body>
  <main class="card">
    <div class="side-band"></div>
    <div class="side-rule"></div>

    <div class="brand">
      <div class="brand-mark"></div>
      <div class="brand-name">Brolvane</div>
    </div>

    <h1 class="person-name">Tomas Ferreira</h1>
    <div class="name-rule"></div>

    <ul class="contacts">
      <li>
        <svg class="contact-icon" viewBox="0 0 30 30" aria-hidden="true">
          <polygon points="15,1 28,8 28,22 15,29 2,22 2,8" fill="#d42328"/>
          <path d="M10 8c1-1 2-1 3 0l1 3c0 1-1 1-1 2 1 2 2 3 4 4 1 0 1-1 2-1l3 1c1 1 1 2 0 3-2 2-5 1-8-2s-6-7-4-10z" fill="#fff"/>
        </svg>
        (555) 014-2287
      </li>
      <li>
        <svg class="contact-icon" viewBox="0 0 30 30" aria-hidden="true">
          <polygon points="15,1 28,8 28,22 15,29 2,22 2,8" fill="#d42328"/>
          <rect x="8" y="10" width="14" height="10" fill="none" stroke="#fff" stroke-width="1.8"/>
          <path d="M8 10l7 6 7-6" fill="none" stroke="#fff" stroke-width="1.8"/>
        </svg>
        brolvanehandyman@example.com
      </li>
    </ul>

    <ul class="services">
      <li>Repair</li>
      <li>Maintain</li>
      <li>Improve</li>
      <li>Remodel</li>
    </ul>

    <p class="tagline">Commercial and Residential, Handyman, Technician</p>
  </main>
</body>
</html>
```